Boutique Financial Services/Advisor Business Needs Web Design

Looking for an informational and functional web design for my Financial Services/Financial Advisement business. It should have functionality for Company name, address, phone #, "About Us", Who we are, Our Mission, Services we offer, Biographies/Photos of/about "The Team", and possibly a link to "Contact Us". Would like to see something new & exciting blended with a traditional/professional look that will appeal to those approaching retirement, as well as those younger clients that are beginning to think about planning for the future. I already have a web domain through HostMeadow, but would like this to be the design we use for that domain.
Financial Services/Financial Advisor
Coded - Design and coding required
1 page

```html
<!DOCTYPE html>
<html lang="en">
<head>
<meta charset="utf-8">
<title>Summit Crest Wealth Management</title>
<link rel="stylesheet" href="https://fonts.googleapis.com/css2?family=Cormorant+Garamond:wght@500;600;700&family=Poppins:wght@300;400;500;600&display=swap">
<style>
:root{
  --navy:#07064a;
  --navy-deep:#04033a;
  --white:#ffffff;
  --ink:#1c1c2a;
  --muted:#4a4a5a;
  --grey:#a6a6ac;
  --line:rgba(255,255,255,.22);
  --serif:"Cormorant Garamond", Georgia, serif;
  --sans:"Poppins", Arial, sans-serif;
}
*{box-sizing:border-box;margin:0;padding:0}
html,body{width:1200px;height:4532px;overflow:hidden}
body{font-family:var(--sans);color:var(--ink);background:var(--white);position:relative}
section,header,footer{position:absolute;left:0;width:1200px}
.serif{font-family:var(--serif)}
.btn{position:absolute;display:inline-flex;align-items:center;gap:10px;height:32px;padding:0 20px;font:500 12px var(--sans);text-decoration:none}
.btn svg{width:14px;height:10px}
.btn-navy{background:var(--navy);color:var(--white)}
.btn-white{background:var(--white);color:var(--navy)}
p.body{font-size:11.5px;line-height:1.75;font-weight:300}

/* hero */
.hero{top:0;height:610px;overflow:hidden}
.hero-photo{position:absolute;inset:0;background:linear-gradient(115deg,#8d8a86 0%,#c9bba6 35%,#6e6560 60%,#2b2a33 100%)}
.hero-shade{position:absolute;inset:0;background:linear-gradient(180deg,rgba(10,10,30,.35),rgba(10,10,30,.65))}
.topline{position:absolute;top:20px;left:60px;right:60px;display:flex;justify-content:space-between;font-size:11px;color:var(--white)}
.topline span{display:flex;align-items:center;gap:7px}
.navbar{position:absolute;top:50px;left:45px;width:1110px;height:56px;background:var(--white);display:flex;align-items:center;padding:0 30px;font-size:12px;font-weight:500;color:var(--ink)}
.navbar .left,.navbar .right{display:flex;gap:34px;align-items:center}
.navbar .right{margin-left:auto}
.navbar .cta{background:var(--navy);color:var(--white);padding:9px 18px}
.brand{position:absolute;top:34px;left:495px;width:210px;height:130px;background:var(--white);display:flex;flex-direction:column;align-items:center;justify-content:center;color:var(--navy);text-align:center}
.brand .name{font:700 24px/1.05 var(--serif);letter-spacing:1px;text-transform:uppercase}
.brand .sub{font:700 13px var(--serif);letter-spacing:3px;text-transform:uppercase;margin-top:4px}
.hero h1{position:absolute;top:300px;left:0;width:1200px;text-align:center;color:var(--white);font:700 60px/1.02 var(--serif)}
.hero p{position:absolute;top:450px;left:250px;width:700px;text-align:center;color:var(--white);font-size:11px;line-height:1.6;font-weight:300}
.hero .btn{top:510px;left:540px}

/* about */
.about{top:610px;height:640px}
.about .photo{position:absolute;left:182px;top:78px;width:410px;height:496px;background:linear-gradient(160deg,#d6dde3,#8a9aa8 55%,#2f3440)}
.play{position:absolute;left:150px;top:120px;width:72px;height:72px;border-radius:50%;background:var(--navy);border:6px solid var(--white)}
.about h2{position:absolute;left:636px;top:110px;width:420px;font:700 46px/1.05 var(--serif);color:var(--ink)}
.about .text{position:absolute;left:636px;top:280px;width:390px}
.about .text p+p{margin-top:14px}
.about .btn{left:636px;top:510px}

/* services */
.services{top:1250px;height:980px;background:var(--navy);color:var(--white)}
.sec-title{position:absolute;left:0;width:1200px;text-align:center;font:600 46px var(--serif)}
.sec-intro{position:absolute;left:270px;width:660px;text-align:center;font-size:11px;line-height:1.6;font-weight:300}
.services .sec-title{top:60px}
.services .sec-intro{top:125px}
.grid{position:absolute;left:182px;top:200px;width:840px;display:grid;grid-template-columns:1fr 1fr;grid-auto-rows:225px}
.cell{padding:28px 30px 0 30px;border-bottom:1px solid var(--line)}
.cell:nth-child(odd){border-right:1px solid var(--line)}
.cell:nth-child(n+5){border-bottom:none}
.cell.active{background:var(--grey)}
.cell h3{display:flex;align-items:center;gap:12px;font:600 25px var(--serif);margin-bottom:12px}
.cell h3 svg{width:18px;height:18px;flex:none}
.cell p{font-size:11px;line-height:1.7;font-weight:300;width:330px}
.services .btn{top:885px;left:540px}

/* strategies */
.strategy{top:2230px;height:640px}
.strategy h2{position:absolute;left:185px;top:125px;width:380px;font:700 46px/1.05 var(--serif)}
.strategy .text{position:absolute;left:185px;top:240px;width:370px}
.strategy .text p+p{margin-top:14px}
.strategy .btn{left:185px;top:440px}
.strategy .photo{position:absolute;left:606px;top:72px;width:400px;height:496px;background:linear-gradient(135deg,#c9b8a3,#8a8078 50%,#3c3a40)}

/* process */
.process{top:2870px;height:530px;background:var(--navy);color:var(--white)}
.process .sec-title{top:50px}
.process .sec-intro{top:115px}
.steps{position:absolute;left:0;top:185px;width:1200px;height:240px}
.step{position:absolute;top:15px;width:210px;height:210px;border-radius:50%;background:var(--white);border:8px solid var(--navy);box-shadow:0 0 0 3px var(--white);color:var(--ink);text-align:center;padding-top:52px}
.step svg{width:22px;height:22px}
.step h4{font:600 13px var(--sans);margin:6px 0 4px}
.step p{font-size:9.5px;line-height:1.5;width:120px;margin:0 auto;color:var(--muted)}
.badge{position:absolute;top:-6px;right:10px;width:48px;height:48px;border-radius:50%;background:var(--grey);border:4px solid var(--navy);display:flex;align-items:center;justify-content:center;font:600 18px var(--serif);color:var(--white)}
.process .btn{top:435px;left:535px}

/* team */
.team{top:3400px;height:630px}
.team .sec-title{top:60px;color:var(--ink)}
.team .sec-intro{top:120px;left:190px;width:820px;color:var(--ink)}
.member{position:absolute;top:210px;width:254px;text-align:center}
.member .photo{height:320px;background:linear-gradient(180deg,#e6ebef,#a8b2bb 55%,#23252d)}
.member h5{font:600 24px var(--serif);margin-top:16px}
.member span{font-size:10px;color:var(--muted)}

/* footer */
.footer{top:4030px;height:502px;background:var(--navy);color:var(--white);text-align:center}
.footer .name{position:absolute;top:55px;left:0;width:1200px;font:700 26px var(--serif);letter-spacing:2px;text-transform:uppercase}
.footer .sub{position:absolute;top:90px;left:0;width:1200px;font:700 14px var(--serif);letter-spacing:4px;text-transform:uppercase}
.footer .blurb{position:absolute;top:160px;left:300px;width:600px;font-size:11px;line-height:1.6;font-weight:300}
.footnav{position:absolute;top:237px;left:240px;width:720px;height:36px;background:var(--grey);display:flex;justify-content:center;align-items:center;gap:46px;font-size:11px;font-weight:500}
.social{position:absolute;top:300px;left:0;width:1200px;display:flex;justify-content:center;gap:12px}
.social span{width:30px;height:30px;border-radius:50%;background:var(--white);color:var(--navy);font:600 9px/30px var(--sans)}
.copy{position:absolute;top:395px;left:0;width:1200px;font-size:10px;font-weight:300}
</style>
</head>
<body>

<section class="hero">
  <div class="hero-photo" role="img" aria-label="Photo of a smiling businesswoman and businessman reviewing documents together"></div>
  <div class="hero-shade"></div>
  <div class="topline">
    <span><svg width="12" height="10" viewBox="0 0 12 10"><rect x=".5" y=".5" width="11" height="9" fill="none" stroke="#fff"/><path d="M.5 .5 6 5.5 11.5 .5" fill="none" stroke="#fff"/></svg>info@summitcrestwealth.com</span>
    <span><svg width="11" height="11" viewBox="0 0 24 24"><path d="M6.6 10.8a15 15 0 0 0 6.6 6.6l2.2-2.2a1 1 0 0 1 1-.25 11.4 11.4 0 0 0 3.6.6 1 1 0 0 1 1 1V20a1 1 0 0 1-1 1A17 17 0 0 1 3 4a1 1 0 0 1 1-1h3.5a1 1 0 0 1 1 1c0 1.25.2 2.45.6 3.6a1 1 0 0 1-.25 1z" fill="#fff"/></svg>(555) 014-2290</span>
  </div>
  <nav class="navbar">
    <div class="left"><span>About Us</span><span>Who we are</span><span>Our Mission</span></div>
    <div class="right"><span>Services</span><span>The Team</span><span class="cta">Contact Us</span></div>
  </nav>
  <div class="brand"><div class="name">Summit Crest</div><div class="sub">Wealth Management</div></div>
  <h1>Guiding You Through Every<br>Financial Milestone</h1>
  <p>We help families and professionals build, protect and grow their wealth with clear plans and steady guidance, from your very first investment through to the day you retire in comfort and confidence.</p>
  <a class="btn btn-white">Contact Us <svg viewBox="0 0 14 10"><path d="M0 5h12M8 1l4 4-4 4" fill="none" stroke="currentColor" stroke-width="1.4"/></svg></a>
</section>

<section class="about">
  <div class="photo" role="img" aria-label="Photo of a bearded financial advisor in a suit"></div>
  <div class="play"><svg width="60" height="60" viewBox="0 0 60 60"><path d="M25 21v18l14-9z" fill="#fff"/></svg></div>
  <h2>Empowering You To Achieve Your Financial Goals</h2>
  <div class="text">
    <p class="body">For over two decades our advisors have partnered with clients at every stage of life. We listen first, learn what matters most to you and your family, and then shape a plan that fits your goals, your timeline and your comfort with risk, reviewing it as life changes.</p>
    <p class="body">Whether you are starting your first savings plan or preparing to step away from work, we bring the same care and attention. Our independent approach means advice that puts your interests first, with honest fees and clear reporting you can always understand.</p>
  </div>
  <a class="btn btn-navy">Learn More <svg viewBox="0 0 14 10"><path d="M0 5h12M8 1l4 4-4 4" fill="none" stroke="currentColor" stroke-width="1.4"/></svg></a>
</section>

<section class="services">
  <h2 class="sec-title">Our Services</h2>
  <p class="sec-intro">From everyday budgeting to multi-generational planning, our services are designed to work together, giving you one trusted team for every part of your financial life and future.</p>
  <div class="grid">
    <div class="cell active">
      <h3><svg viewBox="0 0 18 18"><rect x="2" y="9" width="3" height="7" fill="#fff"/><rect x="7.5" y="5" width="3" height="11" fill="#fff"/><rect x="13" y="2" width="3" height="14" fill="#fff"/></svg>Financial Planning</h3>
      <p>A complete picture of your income, savings, debts and goals, turned into a practical roadmap with clear steps you can follow month by month toward lasting security.</p>
    </div>
    <div class="cell">
      <h3><svg viewBox="0 0 18 18"><path d="M1 15 6 9l4 3 7-9" fill="none" stroke="#fff" stroke-width="2"/></svg>Investment Management</h3>
      <p>Diversified portfolios built around your goals and risk tolerance, monitored daily and rebalanced with discipline so your money keeps working through every market cycle.</p>
    </div>
    <div class="cell">
      <h3><svg viewBox="0 0 18 18"><circle cx="9" cy="9" r="7" fill="none" stroke="#fff" stroke-width="2"/><path d="M9 5v4l3 2" fill="none" stroke="#fff" stroke-width="2"/></svg>Retirement Planning</h3>
      <p>Income strategies that help you know when you can retire, how much you can spend, and how to make your savings last for the many years ahead of you.</p>
    </div>
    <div class="cell">
      <h3><svg viewBox="0 0 18 18"><rect x="3" y="1" width="12" height="16" fill="none" stroke="#fff" stroke-width="2"/><path d="M6 6h6M6 10h6M6 14h3" stroke="#fff" stroke-width="1.6"/></svg>Tax Optimization</h3>
      <p>Thoughtful planning around accounts, withdrawals and giving to reduce what you owe each year and keep more of what you have worked so hard to earn.</p>
    </div>
    <div class="cell">
      <h3><svg viewBox="0 0 18 18"><path d="M2 9 9 2l7 7v7H2z" fill="none" stroke="#fff" stroke-width="2"/></svg>Estate Planning</h3>
      <p>Guidance on wills, trusts and beneficiaries so your wishes are honored and the people and causes you care about are protected for generations to come.</p>
    </div>
    <div class="cell">
      <h3><svg viewBox="0 0 18 18"><rect x="1" y="5" width="16" height="11" fill="none" stroke="#fff" stroke-width="2"/><path d="M6 5V2h6v3" fill="none" stroke="#fff" stroke-width="2"/></svg>Business Financial Services</h3>
      <p>Retirement plans, succession strategies and cash flow advice for owners who want their business to support their family today and well into the future.</p>
    </div>
  </div>
  <a class="btn btn-white">Learn More <svg viewBox="0 0 14 10"><path d="M0 5h12M8 1l4 4-4 4" fill="none" stroke="currentColor" stroke-width="1.4"/></svg></a>
</section>

<section class="strategy">
  <h2>Smart Strategies For Lifelong Success</h2>
  <div class="text">
    <p class="body">Good planning is not a single event. It grows with you. We meet regularly to review your progress, adjust for new goals and keep your plan aligned with the life you want to live, now and later.</p>
    <p class="body">Our team blends time-tested principles with modern tools, giving you secure online access to your accounts, simple reports and an advisor who knows your name and your story.</p>
  </div>
  <a class="btn btn-navy">Learn More <svg viewBox="0 0 14 10"><path d="M0 5h12M8 1l4 4-4 4" fill="none" stroke="currentColor" stroke-width="1.4"/></svg></a>
  <div class="photo" role="img" aria-label="Photo of a smiling couple meeting with an advisor over a laptop"></div>
</section>

<section class="process">
  <h2 class="sec-title">How We Do</h2>
  <p class="sec-intro">Our simple three-step process keeps things clear from the very first conversation, so you always know where you stand and what comes next in your plan.</p>
  <div class="steps">
    <svg width="1200" height="240" style="position:absolute;left:0;top:0"><path d="M300 30 Q360 0 440 40 M520 200 Q600 250 680 200 M760 40 Q840 0 900 30" fill="none" stroke="#fff" stroke-width="2"/></svg>
    <div class="step" style="left:272px"><div class="badge">01</div>
      <svg viewBox="0 0 22 22"><circle cx="11" cy="7" r="4" fill="none" stroke="#07064a" stroke-width="2"/><path d="M3 20c1-5 15-5 16 0" fill="none" stroke="#07064a" stroke-width="2"/></svg>
      <h4>Discover</h4><p>We learn about your goals, family and priorities.</p></div>
    <div class="step" style="left:495px"><div class="badge">02</div>
      <svg viewBox="0 0 22 22"><rect x="2" y="4" width="18" height="14" fill="none" stroke="#07064a" stroke-width="2"/><path d="M2 4l9 7 9-7" fill="none" stroke="#07064a" stroke-width="2"/></svg>
      <h4>Design</h4><p>We build a clear plan tailored to your needs.</p></div>
    <div class="step" style="left:718px"><div class="badge">03</div>
      <svg viewBox="0 0 22 22"><path d="M17 5 5 17M5 8v9h9" fill="none" stroke="#07064a" stroke-width="2"/></svg>
      <h4>Deliver</h4><p>We put it to work and review it with you often.</p></div>
  </div>
  <a class="btn btn-white">Learn More <svg viewBox="0 0 14 10"><path d="M0 5h12M8 1l4 4-4 4" fill="none" stroke="currentColor" stroke-width="1.4"/></svg></a>
</section>

<section class="team">
  <h2 class="sec-title">The Team</h2>
  <p class="sec-intro">Meet the advisors behind every plan. Each brings years of experience, professional credentials and a genuine commitment to helping clients reach their goals with confidence and peace of mind.</p>
  <div class="member" style="left:188px"><div class="photo" role="img" aria-label="Portrait photo of team member John B. in a suit"></div><h5>John B.</h5><span>Senior Advisor</span></div>
  <div class="member" style="left:473px"><div class="photo" role="img" aria-label="Portrait photo of team member Sara J. in a blazer"></div><h5>Sara J.</h5><span>Planning Lead</span></div>
  <div class="member" style="left:756px"><div class="photo" role="img" aria-label="Portrait photo of team member Smith D. in a suit"></div><h5>Smith D.</h5><span>Portfolio Manager</span></div>
</section>

<footer class="footer">
  <div class="name">Summit Crest</div>
  <div class="sub">Wealth Management</div>
  <p class="blurb">Independent financial advice for individuals, families and business owners. Schedule a friendly, no-obligation conversation with our team today.</p>
  <nav class="footnav"><span>About Us</span><span>Who we are</span><span>Our Mission</span><span>Services</span><span>The Team</span><span>Contact Us</span></nav>
  <div class="social"><span>FB</span><span>IG</span></div>
  <p class="copy">Copyright 2024 Summit Crest Wealth Management. All Rights Reserved.</p>
</footer>

</body>
</html>
```